I need package design designs for an organic, natural, unrefined shea butter packaged in a pouch like the example below. The package design should express pure, organic, freshness, moisturizing and healthy. The package design should also reflect the benefits of the product listed below. The product will be called “ORGANIC SHEA BUTTER”
MEANING OF NAME: KERO AFRICA" meaning to Come to Africa for your natural cosmetics
Logo Text/Brand Name:
“KERO”
Logo Styles of Interest:
Elegance
Natural
Organic
Freshness
Unrefined
From a tree nut
Target Market:
General public
Must have:
KISS : Keep it simple stupid
Note: I have a shea nuts stock photo i can provide.
Dimension:W = 7.48 InchesH = 10.43 inches Added Thursday, January 14, 2016
Cosmetics

```html
<!DOCTYPE html>
<html lang="en">
<head>
<meta charset="UTF-8">
<title>KERO Shea Butter Pouch</title>
<link rel="stylesheet" href="https://fonts.googleapis.com/css2?family=Archivo+Black&family=Montserrat:wght@300;400;700&display=swap">
<style>
  :root {
    --canvas-bg: #b3b3b3;
    --pouch-white: #f6f6f6;
    --pouch-edge: #e3e3e3;
    --ink: #111111;
    --seam: #d6d6d6;
    --butter-light: #f1e6b4;
    --butter-mid: #dfcf8a;
    --wood-light: #b9a48c;
    --wood-dark: #6e5a47;
  }
  * { margin: 0; padding: 0; box-sizing: border-box; }
  html, body {
    width: 1200px;
    height: 900px;
    overflow: hidden;
    background: var(--canvas-bg);
  }
  .canvas {
    position: relative;
    width: 1200px;
    height: 900px;
    background: var(--canvas-bg);
  }
  .pouch {
    position: absolute;
    left: 390px;
    top: 128px;
    width: 440px;
    height: 664px;
    background: linear-gradient(90deg, var(--pouch-edge) 0%, var(--pouch-white) 8%, var(--pouch-white) 92%, var(--pouch-edge) 100%);
    overflow: hidden;
  }
  .zip-seam {
    position: absolute;
    left: 0;
    right: 0;
    top: 64px;
    height: 0;
    border-top: 2px solid var(--seam);
  }
  .net-weight {
    position: absolute;
    left: 38px;
    top: 92px;
    font-family: "Montserrat", sans-serif;
    font-weight: 400;
    font-size: 22px;
    color: var(--ink);
  }
  .usage-note {
    position: absolute;
    right: 42px;
    top: 107px;
    font-family: "Montserrat", sans-serif;
    font-weight: 700;
    font-size: 9px;
    letter-spacing: 0.9px;
    color: var(--ink);
  }
  .brand-name {
    position: absolute;
    left: 0;
    right: 0;
    top: 140px;
    text-align: center;
    font-family: "Archivo Black", sans-serif;
    font-size: 52px;
    line-height: 1;
    letter-spacing: 1px;
    color: var(--ink);
  }
  .product-name {
    position: absolute;
    left: 0;
    right: 0;
    top: 205px;
    text-align: center;
    font-family: "Montserrat", sans-serif;
    font-weight: 300;
    font-size: 50px;
    line-height: 1;
    color: var(--ink);
  }
  .product-qualities {
    position: absolute;
    left: 0;
    right: 0;
    top: 280px;
    text-align: center;
    font-family: "Montserrat", sans-serif;
    font-weight: 700;
    font-size: 10px;
    letter-spacing: 1.6px;
    color: var(--ink);
  }
  .product-photo {
    position: absolute;
    left: 0;
    top: 296px;
    width: 440px;
    height: 368px;
  }
</style>
</head>
<body>
  <main class="canvas">
    <section class="pouch">
      <div class="zip-seam"></div>
      <p class="net-weight">16 oz.</p>
      <p class="usage-note">EXTERNAL USE ONLY</p>
      <h1 class="brand-name">KERO</h1>
      <h2 class="product-name">SHEA BUTTER</h2>
      <p class="product-qualities">ORGANIC - UNREFINED - NATURAL</p>
      <svg class="product-photo" viewBox="0 0 440 368" role="img" aria-label="Photo of raw shea butter chunks in a round window, a metal bowl of shea butter with lavender and twine, and shea nuts on a wooden table">
        <defs>
          <linearGradient id="photo-tones" x1="0" y1="0" x2="0" y2="1">
            <stop offset="0" stop-color="var(--butter-light)"/>
            <stop offset="0.55" stop-color="var(--butter-mid)"/>
            <stop offset="0.72" stop-color="var(--wood-light)"/>
            <stop offset="1" stop-color="var(--wood-dark)"/>
          </linearGradient>
        </defs>
        <path fill="url(#photo-tones)" d="M0 250 L72 250 A136 136 0 1 1 368 250 L440 250 L440 368 L0 368 Z"/>
      </svg>
    </section>
  </main>
</body>
</html>
```